For Lease sign for Property management company in Kansas City

We need someone to take our information and design a standard for lease sign that we can put in front of each of our buildings. I would love for it to do its job of letting people know there are units available but also be unique somehow. Also the aspect ratio of the design would ideally be 4 wide by 3 tall but we open to other ideas. It will be a larger yard sign.

Target Market(s)

Potential Tenants

Industry/Entity Type

Real Estate Development

Font styles to use
Sans Serif

Requirements
Must have
• Our logo, our website (www.quillstead-properties.com), our phone number (816) 555-2719.
Nice to have
• Some how say "For Lease"
Sign to be 4' wide by 3' tall
If there was a place to put the building name that would be cool but not ne
Should not have
• Nothing that I can think of

```html
<!DOCTYPE html>
<html lang="en">
<head>
<meta charset="utf-8">
<title>Quillstead Properties – For Lease</title>
<link rel="stylesheet" href="https://fonts.googleapis.com/css2?family=Montserrat:wght@800&family=Roboto:wght@300;400;700;900&display=swap">
<style>
  :root {
    --red: #be1e2d;
    --amber: #f9ae40;
    --charcoal: #58595b;
    --white: #ffffff;
    --blush: #fbf0f0;
    --cream: #fef5ea;
  }
  html, body {
    margin: 0;
    padding: 0;
    overflow: hidden;
    background: var(--white);
  }
  .sign {
    position: relative;
    width: 1200px;
    height: 900px;
    overflow: hidden;
    background: var(--white);
    font-family: "Roboto", Arial, sans-serif;
  }
  .backdrop {
    position: absolute;
    inset: 0;
  }
  .brand {
    position: absolute;
    left: 234px;
    top: 72px;
    display: flex;
    align-items: center;
    gap: 43px;
  }
  .brand-dot {
    width: 206px;
    height: 206px;
    border-radius: 50%;
    background: var(--amber);
    flex: none;
  }
  .brand-name {
    color: var(--red);
    font-weight: 700;
    line-height: 1;
    text-transform: uppercase;
  }
  .brand-name .primary {
    display: block;
    font-size: 78px;
    letter-spacing: -1px;
  }
  .brand-name .secondary {
    display: block;
    font-size: 54px;
    letter-spacing: 8px;
    margin-top: 8px;
  }
  .lease-band {
    position: absolute;
    left: 0;
    top: 321px;
    width: 1200px;
    height: 326px;
    background: var(--red);
  }
  .availability {
    position: absolute;
    left: 88px;
    top: 40px;
    display: flex;
    align-items: center;
    gap: 16px;
  }
  .availability-label {
    color: var(--white);
    font-size: 72px;
    font-weight: 400;
    letter-spacing: -1px;
    line-height: 1;
  }
  .unit-markers {
    display: flex;
    gap: 24px;
    margin-top: 6px;
  }
  .unit-markers span {
    width: 52px;
    height: 52px;
    border-radius: 8px;
    background: var(--amber);
  }
  .headline {
    position: absolute;
    left: 90px;
    top: 112px;
    margin: 0;
    font-size: 190px;
    line-height: 1;
    white-space: nowrap;
  }
  .headline .for {
    color: var(--amber);
    font-weight: 300;
    margin-right: 52px;
  }
  .headline .lease {
    color: var(--white);
    font-weight: 900;
    letter-spacing: 3px;
  }
  .phone {
    position: absolute;
    left: 0;
    top: 647px;
    width: 1200px;
    height: 110px;
    margin: 0;
    display: flex;
    align-items: center;
    justify-content: center;
    font-family: "Montserrat", Arial, sans-serif;
    font-weight: 800;
    font-size: 84px;
    letter-spacing: 3px;
    color: var(--charcoal);
    line-height: 1;
  }
  .web-band {
    position: absolute;
    left: 0;
    top: 757px;
    width: 1200px;
    height: 143px;
    background: var(--amber);
    display: flex;
    align-items: center;
    justify-content: center;
  }
  .website {
    font-family: "Montserrat", Arial, sans-serif;
    font-weight: 800;
    font-size: 56px;
    color: var(--red);
    white-space: nowrap;
    margin-top: -8px;
  }
</style>
</head>
<body>
<main class="sign">
  <svg class="backdrop" width="1200" height="900" viewBox="0 0 1200 900" aria-hidden="true">
    <polygon points="0,40 320,321 0,321" fill="var(--blush)"/>
    <polygon points="1200,120 1200,321 900,321" fill="var(--cream)"/>
    <rect x="0" y="647" width="1200" height="110" fill="var(--blush)"/>
    <polygon points="380,647 1200,647 1200,757 810,757" fill="var(--cream)"/>
    <polygon points="230,757 380,647 690,647 810,757" fill="#f8ebe3"/>
  </svg>

  <header class="brand">
    <div class="brand-dot"></div>
    <div class="brand-name">
      <span class="primary">Quillstead</span>
      <span class="secondary">Properties</span>
    </div>
  </header>

  <section class="lease-band">
    <div class="availability">
      <span class="availability-label">Units Available</span>
      <div class="unit-markers">
        <span></span><span></span><span></span><span></span><span></span><span></span><span></span>
      </div>
    </div>
    <h1 class="headline"><span class="for">FOR</span><span class="lease">LEASE</span></h1>
  </section>

  <p class="phone">(816) 555-2719</p>

  <footer class="web-band">
    <span class="website">www.quillstead-properties.com</span>
  </footer>
</main>
</body>
</html>
```